Brightloom Reach - Business Card

We need a business card for a Social Media Marketing company that specializes in online marketing for small businesses in Canada using common Social Media platforms such as Instagram, Facebook, Snapchat & Twitter.

I have uploaded a copy of our logo which I would like utilized in the business card. We would like the business card to be modern yet classy design.

Our website is www.brightloomreach.ca

Industry/Entity Type

Marketing

Contact Information for Business Card

Email: info@brightloomreach.ca
Website: www.brightloomreach.ca
Telephone: 604-352-9081

Colors

Designer to choose colors to be used in the design.

Requirements
Must have
• Social Media icons on reverse
• Please add some designs with color.

```html
<!DOCTYPE html>
<html lang="en">
<head>
<meta charset="utf-8">
<title>Brightloom Reach – Business Card</title>
<link href="https://fonts.googleapis.com/css2?family=Open+Sans:wght@400;700;800&display=swap" rel="stylesheet">
<style>
  :root {
    --backdrop: #e6e4e1;
    --card-front: #fbfbfa;
    --card-back: #3a3f42;
    --ink: #2b2b2b;
    --ink-soft: #4a4a4a;
    --logo-grey: #4d4f51;
    --logo-light: #e9eaea;
    --accent: #c8102e;
    --icon-ring: #8c9194;
  }
  * { margin: 0; padding: 0; box-sizing: border-box; }
  html, body {
    width: 1200px; height: 844px; overflow: hidden;
    background: var(--backdrop);
    font-family: "Open Sans", Arial, sans-serif;
  }
  .canvas {
    position: relative; width: 1200px; height: 844px;
    display: flex; align-items: center; justify-content: center; gap: 60px;
  }
  .card {
    position: relative; width: 525px; height: 300px; overflow: hidden;
    box-shadow: 0 6px 18px rgba(0,0,0,0.18);
  }
  .card-front { background: var(--card-front); color: var(--ink); }
  .card-back {
    background: var(--card-back);
    display: flex; flex-direction: column; align-items: center; justify-content: center; gap: 26px;
  }
  .accent-bar {
    position: absolute; left: 0; right: 0; bottom: 0; height: 6px;
    background: var(--accent);
  }
  .card-front .accent-bar { top: 0; bottom: auto; left: 0; right: auto; width: 6px; height: 100%; }

  .brand {
    position: absolute; top: 44px; right: 44px;
    display: flex; align-items: center; gap: 12px;
  }
  .brand-square { width: 18px; height: 18px; border: 3px solid var(--accent); }
  .brand-name {
    font-weight: 800; font-size: 30px; line-height: 0.95;
    text-transform: uppercase; color: var(--logo-grey); letter-spacing: 0.5px;
  }

  .person { position: absolute; left: 40px; bottom: 92px; }
  .person-name { font-weight: 700; font-size: 17px; text-transform: uppercase; }
  .person-role { font-size: 14px; color: var(--ink-soft); }

  .contact {
    position: absolute; left: 40px; right: 34px; bottom: 40px;
    display: flex; justify-content: space-between;
    font-size: 13px; color: var(--ink); white-space: nowrap;
  }
  .contact b { font-weight: 700; color: var(--accent); }
  .contact .web { font-weight: 700; }

  .back-name {
    font-weight: 800; font-size: 44px; line-height: 0.95;
    text-transform: uppercase; color: var(--logo-light); text-align: center;
  }
  .social-row { display: flex; gap: 14px; list-style: none; }
  .social-dot {
    width: 26px; height: 26px; border-radius: 50%;
    border: 2px solid var(--icon-ring);
  }
  .social-dot:first-child { border-color: var(--accent); }
</style>
</head>
<body>
<main class="canvas">
  <section class="card card-front" aria-label="Business card front">
    <span class="accent-bar"></span>
    <div class="brand">
      <span class="brand-square"></span>
      <span class="brand-name">Brightloom<br>Reach</span>
    </div>
    <div class="person">
      <p class="person-name">Maren Holt</p>
      <p class="person-role">Managing Director</p>
    </div>
    <div class="contact">
      <span><b>P:</b> 604-352-9081</span>
      <span><b>E:</b> info@brightloomreach.ca</span>
      <span class="web">www.brightloomreach.ca</span>
    </div>
  </section>

  <section class="card card-back" aria-label="Business card back">
    <p class="back-name">Brightloom<br>Reach</p>
    <ul class="social-row" aria-label="Social media profiles">
      <li class="social-dot" role="img" aria-label="Social network profile"></li>
      <li class="social-dot" role="img" aria-label="Social network profile"></li>
      <li class="social-dot" role="img" aria-label="Social network profile"></li>
      <li class="social-dot" role="img" aria-label="Social network profile"></li>
    </ul>
    <span class="accent-bar"></span>
  </section>
</main>
</body>
</html>
```